Dune Air & Plus business card

I need an awesome, double-sided business card designed with our new logo. I would like the one side black with the colored logo, and the back side is all yours. I'd like to see horizontal and vertical layouts. Get creative! Thank you.

Target Market(s)

HVAC, Heating and Cooling in Phoenix, AZ

Industry/Entity Type

HVAC

Contact Information for Business Card

We need our new logo on the card. Tom Harker, (623) 555-0142, tom@trydunesair.com, www.trydunesair.com, ROC 514273

```html
<!DOCTYPE html>
<html lang="en">
<head>
<meta charset="utf-8">
<title>Dune Air &amp; Plus business card</title>
<link rel="stylesheet" href="https://fonts.googleapis.com/css2?family=Montserrat:wght@400;500;800&display=swap">
<style>
  :root {
    --page: #e4e4e4;
    --card: #231f20;
    --blue-light: #3a82c6;
    --blue-dark: #1a5da8;
    --blue-text: #1e6bbd;
    --orange: #f28c22;
    --red: #d8332a;
    --icon: #e4572e;
    --white: #ffffff;
    --divider: #8a8a8a;
  }
  * { margin: 0; padding: 0; box-sizing: border-box; }
  html, body {
    width: 1200px; height: 960px; overflow: hidden;
    background: var(--page);
    font-family: "Montserrat", Arial, sans-serif;
  }
  .canvas { position: relative; width: 1200px; height: 960px; }
  .card {
    position: absolute; left: 298px; width: 609px; height: 348px;
    background: var(--card); overflow: hidden;
    box-shadow: 4px 5px 8px rgba(0,0,0,0.35);
  }
  .card-front { top: 107px; }
  .card-back { top: 508px; }

  .band { position: absolute; top: 116px; height: 115px; }
  .band-cool { left: 0; width: 142px; background: linear-gradient(90deg, var(--blue-light), var(--blue-dark)); }
  .band-warm { right: 0; width: 137px; background: linear-gradient(90deg, var(--orange), var(--red)); }

  .brand-mark {
    position: absolute; left: 50%; border-radius: 50%;
    background: linear-gradient(90deg, var(--blue-dark) 0 50%, var(--orange) 50% 100%);
  }
  .card-front .brand-mark { width: 96px; height: 96px; margin-left: -48px; top: 48px; }

  .brand-name-front {
    position: absolute; left: 142px; right: 137px; top: 150px;
    text-align: center; font-weight: 800; font-size: 44px; line-height: 48px;
    letter-spacing: 1.5px; color: var(--blue-text); text-transform: uppercase;
  }

  .holder { position: absolute; right: 324px; top: 60px; text-align: right; }
  .holder-name {
    font-weight: 800; font-size: 17px; color: var(--blue-text);
    letter-spacing: 0.5px; text-transform: uppercase; line-height: 22px;
  }
  .holder-licence { font-size: 15px; color: var(--white); line-height: 22px; }

  .divider {
    position: absolute; left: 303px; top: 54px; width: 2px; height: 61px;
    background: var(--divider);
  }

  .contacts { position: absolute; left: 322px; top: 53px; list-style: none; }
  .contacts li {
    display: flex; align-items: center; gap: 5px;
    font-size: 15px; color: var(--white); line-height: 21px;
  }
  .contacts svg { width: 13px; height: 13px; flex: none; }

  .card-back .brand-mark { width: 110px; height: 110px; margin-left: -55px; top: 158px; }
  .brand-name-back {
    position: absolute; left: 0; right: 0; top: 280px;
    text-align: center; font-weight: 800; font-size: 44px; line-height: 48px;
    letter-spacing: 1.5px; color: var(--blue-text); text-transform: uppercase;
  }
</style>
</head>
<body>
<main class="canvas">
  <section class="card card-front" aria-label="Card front">
    <div class="band band-cool"></div>
    <div class="band band-warm"></div>
    <div class="brand-mark" aria-hidden="true"></div>
    <p class="brand-name-front">Dune Air<br>&amp; Plus</p>
  </section>

  <section class="card card-back" aria-label="Card back">
    <div class="holder">
      <p class="holder-name">Tom Harker</p>
      <p class="holder-licence">ROC 514273</p>
    </div>
    <div class="divider"></div>
    <ul class="contacts">
      <li>
        <svg viewBox="0 0 16 16" aria-hidden="true"><path fill="var(--icon)" d="M3.5 1.5l2.5 0 1 3.5-1.8 1.2a8 8 0 0 0 4.6 4.6L11 9l3.5 1v2.5c0 1-1 2-2 2A11 11 0 0 1 1.5 3.5c0-1 1-2 2-2z"/></svg>
        (623) 555-0142
      </li>
      <li>
        <svg viewBox="0 0 16 16" aria-hidden="true"><rect x="1" y="3" width="14" height="10" fill="var(--icon)"/><path d="M1.5 3.5L8 9l6.5-5.5" stroke="var(--card)" stroke-width="1.4" fill="none"/></svg>
        tom@trydunesair.com
      </li>
      <li>
        <svg viewBox="0 0 16 16" aria-hidden="true"><g fill="none" stroke="var(--icon)" stroke-width="1.4"><circle cx="8" cy="8" r="6.5"/><ellipse cx="8" cy="8" rx="2.8" ry="6.5"/><path d="M1.5 8h13M2.5 5h11M2.5 11h11"/></g></svg>
        www.trydunesair.com
      </li>
    </ul>
    <div class="brand-mark" aria-hidden="true"></div>
    <p class="brand-name-back">Dune Air &amp; Plus</p>
  </section>
</main>
</body>
</html>
```